Business Card Design

I would like a new business card that incorporates the new colors and font of the attached DKM4x10.pdf file of our new sign (latte & luxurious red from Kelvane Fairbrook colors) with the logo from the old business card (file name is New2014.pdf). You can remove the phrases from the old card, and just use the contact info provided above. Please let me know if you have any questions.

Industry/Entity Type

Business

Contact Information for Business Card

Dana Kay Morrow, LLC
Real Estate Attorney
842 Larkspur Street
Pine Hollow, GA 30777
(O) 555-203-4179
(C) 555-372-9051
dana@dkmlawoffice.com
dkmlawoffice.com

```html
<!DOCTYPE html>
<html lang="en">
<head>
<meta charset="utf-8">
<title>Dana Kay Morrow, LLC — Business Card</title>
<link href="https://fonts.googleapis.com/css2?family=Open+Sans:wght@400;600&display=swap" rel="stylesheet">
<style>
  :root {
    --backdrop: #e4dfd8;
    --card: #151515;
    --card-edge: #0c0c0c;
    --accent: #c23a4b;
    --ink: #f2f2f2;
    --muted: #d8d8d8;
  }
  html, body {
    margin: 0;
    padding: 0;
    width: 1200px;
    height: 844px;
    overflow: hidden;
    background: var(--backdrop);
    font-family: "Open Sans", Arial, sans-serif;
  }
  .stage {
    position: relative;
    width: 1200px;
    height: 844px;
    display: flex;
    align-items: center;
    justify-content: center;
    gap: 40px;
  }
  .card {
    position: relative;
    width: 540px;
    height: 309px;
    background: var(--card);
    border: 1px solid var(--card-edge);
    box-shadow: 0 10px 28px rgba(0,0,0,0.22);
    box-sizing: border-box;
  }
  .brand {
    position: absolute;
    left: 0;
    right: 0;
    display: flex;
    align-items: center;
    justify-content: center;
    gap: 12px;
  }
  .brand-mark {
    width: 18px;
    height: 18px;
    background: var(--accent);
  }
  .brand-name {
    color: var(--accent);
    font-weight: 600;
    font-size: 28px;
    letter-spacing: 0.2px;
  }
  .card--front .brand { top: 58px; }
  .card--back .brand { top: 112px; }

  .identity {
    position: absolute;
    left: 40px;
    bottom: 34px;
    width: 230px;
    text-align: right;
    color: var(--ink);
    font-size: 16px;
    line-height: 24px;
  }
  .identity-name {
    color: var(--accent);
    font-size: 19px;
    line-height: 28px;
  }
  .contact {
    position: absolute;
    left: 300px;
    top: 150px;
    margin: 0;
    padding: 0;
    list-style: none;
    color: var(--muted);
    font-size: 15px;
    line-height: 24px;
  }
  .contact-item {
    display: flex;
    align-items: center;
    gap: 10px;
  }
  .contact-icon {
    width: 12px;
    height: 12px;
    flex: none;
  }
  .website {
    position: absolute;
    left: 0;
    right: 0;
    top: 168px;
    text-align: center;
    color: var(--accent);
    font-size: 15px;
    font-weight: 600;
    letter-spacing: 1px;
  }
</style>
</head>
<body>
<main class="stage">
  <section class="card card--front" aria-label="Card front">
    <div class="brand">
      <span class="brand-mark"></span>
      <span class="brand-name">Dana Kay Morrow</span>
    </div>

    <div class="identity">
      <div class="identity-name">Dana Kay Morrow, LLC</div>
      <div>Real Estate Attorney</div>
      <div>842 Larkspur Street</div>
      <div>Pine Hollow, GA 30777</div>
    </div>

    <ul class="contact">
      <li class="contact-item">
        <svg class="contact-icon" viewBox="0 0 12 12" aria-hidden="true"><path d="M2 1 L4 1 L5 3.5 L3.8 4.5 Q5 7 7.5 8.2 L8.5 7 L11 8 L11 10 Q10 11 8.5 11 Q2 9.5 1 3 Q1 1.5 2 1 Z" fill="var(--accent)"/></svg>
        <span>555-203-4179</span>
      </li>
      <li class="contact-item">
        <svg class="contact-icon" viewBox="0 0 12 12" aria-hidden="true"><rect x="3" y="0.8" width="6" height="10.4" rx="1" fill="none" stroke="var(--accent)" stroke-width="1.2"/><rect x="5.2" y="9" width="1.6" height="1" fill="var(--accent)"/></svg>
        <span>555-372-9051</span>
      </li>
      <li class="contact-item">
        <svg class="contact-icon" viewBox="0 0 12 12" aria-hidden="true"><rect x="0.5" y="2.5" width="11" height="7.5" fill="var(--accent)"/><path d="M0.8 2.8 L6 6.8 L11.2 2.8" fill="none" stroke="var(--card)" stroke-width="1"/></svg>
        <span>dana@dkmlawoffice.com</span>
      </li>
      <li class="contact-item">
        <svg class="contact-icon" viewBox="0 0 12 12" aria-hidden="true"><g fill="none" stroke="var(--accent)" stroke-width="1.4"><rect x="0.8" y="5" width="5.5" height="3.2" rx="1.6" transform="rotate(-45 3.5 6.6)"/><rect x="5.7" y="3.8" width="5.5" height="3.2" rx="1.6" transform="rotate(-45 8.5 5.4)"/></g></svg>
        <span>www.dkmlawoffice.com</span>
      </li>
    </ul>
  </section>

  <section class="card card--back" aria-label="Card back">
    <div class="brand">
      <span class="brand-mark"></span>
      <span class="brand-name">Dana Kay Morrow</span>
    </div>
    <div class="website">www.dkmlawoffice.com</div>
  </section>
</main>
</body>
</html>
```